Income Tax Business Cards - Updates

Need to update these business cards while keeping all the same wording but just update them and make them look nicer and more modern/ on brand with our brand.

Industry/Entity Type

finance

Contact Information for Business Card

we have multiple locations so will just need to easily be able to change the address and phone numbers

Colors

Designer to choose colors to be used in the design.

```html
<!DOCTYPE html>
<html lang="en">
<head>
<meta charset="utf-8">
<title>Tax Advance Business Card</title>
<link href="https://fonts.googleapis.com/css2?family=Lilita+One&family=Montserrat:wght@800;900&display=swap" rel="stylesheet">
<style>
  :root {
    --green: #115130;
    --red: #c1262b;
    --white: #ffffff;
    --paper: #ffffff;
  }
  html, body {
    margin: 0;
    padding: 0;
    width: 1073px;
    height: 1200px;
    overflow: hidden;
    background: var(--paper);
  }
  .sheet {
    position: relative;
    width: 1073px;
    height: 1200px;
  }
  .card {
    position: absolute;
    left: 75px;
    width: 906px;
    height: 519px;
    filter: drop-shadow(6px 7px 5px rgba(0,0,0,0.35));
  }
  .card--front { top: 47px; }
  .card--back { top: 624px; }
  .card svg { display: block; width: 100%; height: 100%; }
  .fill-green { fill: var(--green); }
  .fill-red { fill: var(--red); }
  .fill-white { fill: var(--white); }
  .display {
    font-family: "Lilita One", "Arial Black", sans-serif;
    text-anchor: middle;
    letter-spacing: 1px;
  }
  .headline {
    font-family: "Montserrat", Arial, sans-serif;
    font-weight: 900;
    text-anchor: middle;
  }
  .contact {
    font-family: "Montserrat", Arial, sans-serif;
    font-weight: 800;
    fill: var(--red);
  }
  .brand-name {
    font-family: "Montserrat", Arial, sans-serif;
    font-weight: 800;
    fill: var(--green);
    text-anchor: middle;
  }
</style>
</head>
<body>
<main class="sheet">

  <!-- Front side -->
  <section class="card card--front" aria-label="Card front">
    <svg viewBox="0 0 1216 696" xmlns="http://www.w3.org/2000/svg">
      <rect class="fill-white" width="1216" height="696"/>
      <!-- top stripes -->
      <polygon class="fill-green" points="355,0 420,0 510,77 445,77"/>
      <polygon class="fill-red" points="475,0 635,0 725,77 565,77"/>
      <polygon class="fill-green" points="715,0 790,0 880,77 805,77"/>
      <polygon class="fill-red" points="815,0 915,0 1005,77 905,77"/>
      <!-- main band -->
      <rect class="fill-green" x="0" y="77" width="1216" height="542"/>
      <!-- bottom stripes -->
      <polygon class="fill-green" points="530,619 590,619 670,696 610,696"/>
      <polygon class="fill-red" points="610,619 650,619 730,696 690,696"/>
      <!-- corner wedge -->
      <polygon class="fill-red" points="0,455 245,696 0,696"/>
      <!-- side diamonds -->
      <polygon class="fill-red" points="0,270 80,348 0,428" stroke="#fff" stroke-width="5"/>
      <polygon class="fill-red" points="1216,270 1136,348 1216,428" stroke="#fff" stroke-width="5"/>

      <text class="headline fill-white" x="610" y="197" font-size="92">FILE YOUR</text>
      <text class="display" x="610" y="308" font-size="100" fill="#c1262b" stroke="#fff" stroke-width="6" paint-order="stroke">TAXES HERE</text>
      <line x1="245" y1="357" x2="970" y2="357" stroke="#fff" stroke-width="3"/>
      <text class="display" x="610" y="485" font-size="104" fill="#115130" stroke="#fff" stroke-width="7" paint-order="stroke">UP TO $6,000</text>
      <text class="display" x="610" y="577" font-size="66" fill="#115130" stroke="#fff" stroke-width="6" paint-order="stroke">AME DAY ADVANCE</text>
    </svg>
  </section>

  <!-- Back side -->
  <section class="card card--back" aria-label="Card back">
    <svg viewBox="0 0 1216 696" xmlns="http://www.w3.org/2000/svg">
      <rect class="fill-white" width="1216" height="696"/>
      <!-- top band -->
      <rect class="fill-green" x="0" y="0" width="1216" height="85"/>
      <polygon class="fill-white" points="530,0 585,0 665,85 610,85"/>
      <polygon class="fill-red" points="650,0 820,0 900,85 730,85"/>
      <polygon class="fill-white" points="895,0 935,0 1015,85 975,85"/>
      <polygon class="fill-red" points="990,0 1090,0 1170,85 1070,85"/>
      <!-- sweeping band into estimate panel -->
      <polygon class="fill-green" points="0,137 605,137 785,305 1216,305 1216,470 805,470 580,195 0,195"/>
      <!-- corner wedge -->
      <polygon class="fill-green" points="0,430 285,696 0,696"/>
      <!-- bottom stripes -->
      <polygon class="fill-red" points="365,608 530,608 620,696 455,696"/>
      <polygon class="fill-red" points="610,608 665,608 750,696 695,696"/>

      <!-- brand -->
      <text class="brand-name" x="1000" y="215" font-size="46">Ledgerline</text>
      <text class="brand-name" x="1000" y="262" font-size="26" letter-spacing="4">FINANCIAL GROUP</text>

      <text class="display" x="340" y="352" font-size="90" fill="#c1262b" stroke="#c1262b" stroke-width="12" paint-order="stroke">UP TO $6,000</text>
      <text class="display" x="340" y="352" font-size="90" fill="#c1262b" stroke="#fff" stroke-width="5" paint-order="stroke">UP TO $6,000</text>
      <text class="display" x="340" y="420" font-size="54" fill="#c1262b" stroke="#c1262b" stroke-width="10" paint-order="stroke">SAME DAY ADVANCE</text>
      <text class="display" x="340" y="420" font-size="54" fill="#c1262b" stroke="#fff" stroke-width="4" paint-order="stroke">SAME DAY ADVANCE</text>
      <text class="headline fill-green" x="340" y="468" font-size="30">ON APPROVED TAX RETURNS!</text>

      <text class="headline fill-white" x="995" y="372" font-size="50">FREE</text>
      <text class="headline fill-white" x="1000" y="440" font-size="50">ESTIMATES!</text>

      <!-- phone -->
      <rect class="fill-red" x="833" y="508" width="42" height="42" rx="8"/>
      <path d="M845 518c2-2 5-2 6 0l3 5c1 2 0 3-1 4l-2 1c1 4 4 7 8 8l1-2c1-1 2-2 4-1l5 3c2 1 2 4 0 6l-2 2c-8 2-22-12-22-22z" fill="#fff"/>
      <text class="contact" x="890" y="542" font-size="35">(555) 555-5555</text>

      <!-- addresses -->
      <g>
        <rect class="fill-red" x="836" y="566" width="32" height="32" rx="6"/>
        <path d="M852 572a7 7 0 0 1 7 7c0 5-7 12-7 12s-7-7-7-12a7 7 0 0 1 7-7z" fill="none" stroke="#fff" stroke-width="2.5"/>
        <text class="contact" x="882" y="592" font-size="29">Address 1</text>
      </g>
      <g>
        <rect class="fill-red" x="836" y="604" width="32" height="32" rx="6"/>
        <path d="M852 610a7 7 0 0 1 7 7c0 5-7 12-7 12s-7-7-7-12a7 7 0 0 1 7-7z" fill="none" stroke="#fff" stroke-width="2.5"/>
        <text class="contact" x="882" y="630" font-size="29">Address 2</text>
      </g>
      <g>
        <rect class="fill-red" x="836" y="642" width="32" height="32" rx="6"/>
        <path d="M852 648a7 7 0 0 1 7 7c0 5-7 12-7 12s-7-7-7-12a7 7 0 0 1 7-7z" fill="none" stroke="#fff" stroke-width="2.5"/>
        <text class="contact" x="882" y="668" font-size="29">Address 3</text>
      </g>
    </svg>
  </section>

</main>
</body>
</html>
```